Vitalquorra.com

I need a web design for a Online Wellness Center based in Chicago, IL and it's called "Vitalquorra" We provide Health risk assessment to individuals and interventions. Our portal has a Health Activity tracker where our members record health activities and aerobic miles and biometric data. Our Online wellness center tracks the participant's progress toward health goals and awards points for completed activities.
I started working on this website but the designer was not able to designer a website which describes what we do. I need a fresh look on this project. I need a very attractive, responsive website which says what we do.
These are the things we do.
1. We provide Health Risk Assessments to individuals and Co-operations
2. We Provide Free health screenings to undeserved communities
3. Assist individuals access free or affordable medications
4. We ask providers/doctors to see (or do a complete physical) one individual free of charge once a year (those individuals who are no insured and don't have money to pay from their pocket)
5. Assist patient access lab work at low cost
Our goal is to provide services that will lower the cost of care for our members.

Here is the website: www.vitalquorra.com still underdevelopment. PLEASE DO NOT COPY THIS STYLE OF WEBSITE. IT'S A BAD DESIGN AND THAT IS WHY I'M RE-DESIGNING THE SITE

Target Market(s)

Health individuals between the age of 21 to 65 Plus years old. Insured and uninsured

Industry/Entity Type

Health And Wellness

Coding

Coded - Design and coding required

Number of Pages Required

5+ page

Colors
0292cd

Requirements
Must have
• I'm still working on this websiteHere is the menu: Home, About us, Services, Health Screening, Providers, Contacts
• Please see. www.vitalquorra.com
Nice to have
• Event calender
• Upcoming Event
• Medication
• Lab assist
• Providers/Free Clinics

```html
<!DOCTYPE html>
<html lang="en">
<head>
<meta charset="utf-8">
<title>Vitalquorra – Online Wellness Center</title>
<link href="https://fonts.googleapis.com/css2?family=Open+Sans:wght@400;600;700&display=swap" rel="stylesheet">
<style>
:root{
  --brand:#0292cd;
  --brand-dark:#0a6fa0;
  --ink:#333;
  --muted:#777;
  --line:#d6d6d6;
  --paper:#fff;
  --soft:#f3f3f3;
  --footer:#3a3a3a;
  --footer-deep:#2a2a2a;
}
*{box-sizing:border-box;margin:0;padding:0}
html,body{width:1200px;height:2496px;overflow:hidden}
body{font-family:"Open Sans",Arial,sans-serif;color:var(--ink);background:var(--paper);font-size:13px;line-height:1.55}
.wrap{width:880px;margin:0 auto;position:relative}

/* header */
.topbar{height:72px}
.topbar .wrap{display:flex;justify-content:space-between;align-items:center;height:72px}
.brand{display:flex;align-items:center;gap:10px;font-size:26px;font-weight:700;color:var(--brand)}
.brand i{width:22px;height:22px;border-radius:50%;background:var(--brand);display:block}
.contact-mini{font-size:11px;color:var(--muted);text-align:left;line-height:1.6}
.nav{height:24px;background:var(--brand)}
.nav ul{list-style:none;display:flex;height:24px}
.nav li{font-size:12px;color:#fff;padding:0 18px;line-height:24px}
.nav li.active{background:var(--brand-dark)}

/* hero */
.hero{height:544px;position:relative;background:linear-gradient(90deg,#3d7ea9 0%,#6ea2c6 40%,#b9d2e3 70%,#8fb4cf 100%)}
.hero .photo{position:absolute;inset:0}
.appoint{position:absolute;left:160px;top:32px;width:370px;height:440px;background:rgba(20,60,95,.55)}
.appoint h2{background:var(--brand);color:#fff;font-size:22px;font-weight:600;width:270px;height:52px;line-height:52px;padding-left:24px}
.appoint form{padding:28px 24px 0}
.field{display:block;width:240px;height:26px;background:#fff;margin-bottom:14px;font-size:11px;color:#999;padding:4px 10px}
.appoint .btn{display:inline-block;margin-top:110px;background:var(--brand);color:#fff;font-size:12px;padding:6px 22px}

/* features */
.features{padding-top:40px;height:260px}
.features .wrap{display:flex;justify-content:space-between}
.feature{width:260px;position:relative}
.feature .disc{width:64px;height:64px;border-radius:50%;background:var(--brand);border:4px solid #cfe9f5;display:flex;align-items:center;justify-content:center;margin:0 auto 22px}
.feature .body{border-left:2px dashed var(--line);border-bottom:2px dashed var(--line);padding:0 0 14px 18px;margin-left:28px}
.feature h3{font-size:14px;color:var(--brand);font-weight:600}
.feature p{font-size:11px;color:var(--muted)}

/* section title */
.section-title{font-size:22px;font-weight:700;color:#222;display:flex;align-items:center;gap:16px;margin-bottom:16px}
.section-title::after{content:"";flex:1;height:1px;background:var(--line)}

/* events */
.events{height:650px}
.event{display:flex;height:184px;margin-bottom:6px}
.event .pic{width:440px;height:184px;position:relative;background:linear-gradient(120deg,#b99a80,#d8c6b4 50%,#8fa6b8)}
.event.b .pic{background:linear-gradient(120deg,#9fb9cc,#e6edf2 50%,#7d94a8)}
.event.c .pic{background:linear-gradient(120deg,#c7a68e,#e9ddd1 50%,#a89080)}
.date{position:absolute;right:0;top:34px;width:150px;height:110px;background:rgba(255,255,255,.35);color:#fff;text-align:center;padding-top:14px}
.date b{display:block;font-size:44px;font-weight:400;line-height:1.1}
.date span{font-size:18px}
.event .text{width:440px;padding:6px 24px}
.event .text h4{font-size:16px;color:var(--brand);font-weight:600;margin-bottom:4px}
.event .text p{font-size:11px;color:var(--muted)}
.more{font-size:11px;color:var(--brand);display:block;margin-top:8px}

/* services */
.services{height:260px}
.services .wrap{display:flex;justify-content:space-between;padding-top:10px}
.service{width:270px}
.service .ico{width:40px;height:40px;background:var(--brand);display:flex;align-items:center;justify-content:center;margin-bottom:10px}
.service h3{font-size:15px;font-weight:700;color:#222}
.service p{font-size:11px;color:var(--muted);margin:4px 0 12px}
.service .btn{display:inline-block;background:var(--brand);color:#fff;font-size:10px;padding:4px 14px}

/* testimonials */
.testimonials{height:320px}
.cards{display:flex;justify-content:space-between}
.card{width:430px;height:216px;border:1px solid var(--line);background:var(--soft);display:flex;padding:10px}
.card .face{width:170px;height:194px;background:linear-gradient(160deg,#d9c3b0,#a88a74 60%,#e8e1da)}
.card.two .face{background:linear-gradient(160deg,#e5ebef,#b5c4cf 60%,#8fa3b3)}
.card .quote{flex:1;padding:8px 14px;font-size:11px;color:var(--muted);position:relative}
.card .quote .mark{font-size:34px;color:#aaa;line-height:.6;display:block}
.card .name{margin-top:6px;font-weight:600;color:#555}
.social{display:flex;align-items:center;gap:6px;font-size:11px;color:#555;position:absolute;bottom:4px;right:14px}
.social i{width:20px;height:20px;background:var(--brand);display:block}

/* footer */
.footer{background:var(--footer);color:#ccc;height:268px;padding-top:24px}
.footer .wrap{display:flex;gap:80px}
.footer h4{color:#fff;font-size:15px;font-weight:600;border-bottom:1px solid #555;padding-bottom:8px;margin-bottom:14px}
.about{width:470px;font-size:11px}
.about .social{position:static;margin-top:28px;color:#ccc}
.about .social i{border-radius:50%;background:#555}
.reach{width:260px;font-size:11px}
.reach li{list-style:none;display:flex;gap:10px;margin-bottom:6px}
.copyright{background:var(--footer-deep);height:48px;line-height:48px;text-align:center;font-size:10px;color:#aaa}
</style>
</head>
<body>

<header class="topbar">
  <div class="wrap">
    <div class="brand"><i></i>Vitalquorra</div>
    <div class="contact-mini">Call for Enquiry: +1 (312) 555 0148<br>info@vitalquorra.com</div>
  </div>
</header>
<nav class="nav">
  <div class="wrap">
    <ul>
      <li class="active">Home</li><li>About us</li><li>Services</li><li>Health Screening</li><li>Providers</li><li>Contacts</li>
    </ul>
  </div>
</nav>

<section class="hero">
  <div class="photo" role="img" aria-label="Smiling doctor in a white coat holding a clipboard in a bright clinic corridor"></div>
  <div class="appoint">
    <h2>Fix An Appointment</h2>
    <form>
      <span class="field">Name</span>
      <span class="field">E-mail</span>
      <span class="field">Phone</span>
      <span class="field">Date - MM/DD/YYYY</span>
      <span class="btn">Submit</span>
    </form>
  </div>
</section>

<section class="features">
  <div class="wrap">
    <div class="feature">
      <div class="disc"><svg width="26" height="26" viewBox="0 0 24 24"><path d="M12 21s-8-5-8-11a4.5 4.5 0 0 1 8-2.8A4.5 4.5 0 0 1 20 10c0 6-8 11-8 11z" fill="#fff"/></svg></div>
      <div class="body"><h3>Lorem Ipsum</h3><p>Lorem Ipsum is simply dummy text of the printing and typesetting industry. Lorem Ipsum has been the industry's standard dummy text.</p></div>
    </div>
    <div class="feature">
      <div class="disc"><svg width="26" height="26" viewBox="0 0 24 24"><path d="M10 3h4v7h7v4h-7v7h-4v-7H3v-4h7z" fill="#fff"/></svg></div>
      <div class="body"><h3>Lorem Ipsum</h3><p>Lorem Ipsum is simply dummy text of the printing and typesetting industry. Lorem Ipsum has been the industry's standard dummy text.</p></div>
    </div>
    <div class="feature">
      <div class="disc"><svg width="26" height="26" viewBox="0 0 24 24"><circle cx="12" cy="12" r="8" fill="none" stroke="#fff" stroke-width="2"/><path d="M12 7v5l3 3" stroke="#fff" stroke-width="2" fill="none"/></svg></div>
      <div class="body"><h3>Lorem Ipsum</h3><p>Lorem Ipsum is simply dummy text of the printing and typesetting industry. Lorem Ipsum has been the industry's standard dummy text.</p></div>
    </div>
  </div>
</section>

<section class="events">
  <div class="wrap">
    <h2 class="section-title">Events</h2>
    <div class="event a">
      <div class="pic" role="img" aria-label="Family of three smiling together outdoors"><div class="date"><b>21</b><span>August</span></div></div>
      <div class="text"><h4>Lorem Ipsum</h4><p>Lorem Ipsum is simply dummy text of the printing and typesetting industry. Lorem Ipsum has been the industry's standard dummy text ever since the 1500s, when an unknown printer took a galley of type and scrambled it to make a type specimen book. It has survived not only five centuries but also the leap.</p><span class="more">Read More</span></div>
    </div>
    <div class="event b">
      <div class="text"><h4>Lorem Ipsum</h4><p>Lorem Ipsum is simply dummy text of the printing and typesetting industry. Lorem Ipsum has been the industry's standard dummy text ever since the 1500s, when an unknown printer took a galley of type and scrambled it to make a type specimen book. It has survived not only five centuries but also the leap.</p><span class="more">Read More</span></div>
      <div class="pic" role="img" aria-label="Group of medical staff in scrubs standing together"><div class="date"><b>22</b><span>March</span></div></div>
    </div>
    <div class="event c">
      <div class="pic" role="img" aria-label="Couple smiling with their young child"><div class="date"><b>12</b><span>March</span></div></div>
      <div class="text"><h4>Lorem Ipsum</h4><p>Lorem Ipsum is simply dummy text of the printing and typesetting industry. Lorem Ipsum has been the industry's standard dummy text ever since the 1500s, when an unknown printer took a galley of type and scrambled it to make a type specimen book. It has survived not only five centuries but also the leap.</p><span class="more">Read More</span></div>
    </div>
  </div>
</section>

<section class="services">
  <div class="wrap">
    <div class="service">
      <div class="ico"><svg width="22" height="22" viewBox="0 0 24 24"><path d="M3 11l9-8 9 8v10h-6v-6H9v6H3z" fill="#fff"/></svg></div>
      <h3>Lorem Ipsum is simply</h3><p>Lorem Ipsum is simply dummy text of the printing and typesetting industry. Lorem Ipsum has been the industry's.</p><span class="btn">Read More</span>
    </div>
    <div class="service">
      <div class="ico"><svg width="22" height="22" viewBox="0 0 24 24"><rect x="3" y="5" width="18" height="16" fill="none" stroke="#fff" stroke-width="2"/><path d="M3 10h18M8 3v4M16 3v4" stroke="#fff" stroke-width="2"/></svg></div>
      <h3>Lorem Ipsum is simply</h3><p>Lorem Ipsum is simply dummy text of the printing and typesetting industry. Lorem Ipsum has been the industry's.</p><span class="btn">Read More</span>
    </div>
    <div class="service">
      <div class="ico"><svg width="22" height="22" viewBox="0 0 24 24"><path d="M12 2a7 7 0 0 0-7 7c0 5 7 13 7 13s7-8 7-13a7 7 0 0 0-7-7zm0 10a3 3 0 1 1 0-6 3 3 0 0 1 0 6z" fill="#fff"/></svg></div>
      <h3>Lorem Ipsum is simply</h3><p>Lorem Ipsum is simply dummy text of the printing and typesetting industry. Lorem Ipsum has been the industry's.</p><span class="btn">Read More</span>
    </div>
  </div>
</section>

<section class="testimonials">
  <div class="wrap">
    <h2 class="section-title">Testimonials</h2>
    <div class="cards">
      <div class="card">
        <div class="face" role="img" aria-label="Portrait of a smiling woman with dark hair"></div>
        <div class="quote"><span class="mark">&ldquo;</span>Lorem Ipsum is simply dummy text of the printing and typesetting industry. Lorem Ipsum has been the industry's standard dummy text ever since the 1500s, when an unknown printer took a galley.<div class="name">- Lorem</div>
          <div class="social">Social Links: <i></i><i></i><i></i></div></div>
      </div>
      <div class="card two">
        <div class="face" role="img" aria-label="Portrait of a doctor in a white coat"></div>
        <div class="quote"><span class="mark">&ldquo;</span>Lorem Ipsum is simply dummy text of the printing and typesetting industry. Lorem Ipsum has been the industry's standard dummy text ever since the 1500s, when an unknown printer took a galley.<div class="name">- Lorem</div>
          <div class="social">Social Links: <i></i><i></i><i></i></div></div>
      </div>
    </div>
  </div>
</section>

<footer class="footer">
  <div class="wrap">
    <div class="about">
      <h4>About Us</h4>
      <p>Lorem Ipsum is simply dummy text of the printing and typesetting industry. Lorem Ipsum has been the industry's standard dummy text ever since the 1500s, when an unknown printer took a galley of type and scrambled it to make a type specimen book. It has survived not only five centuries but also the leap into electronic typesetting, remaining essentially unchanged.</p>
      <div class="social">Social Links: <i></i><i></i><i></i><i></i></div>
    </div>
    <div class="reach">
      <h4>Contact</h4>
      <ul>
        <li><svg width="12" height="14" viewBox="0 0 24 24"><path d="M6 2h4l2 5-3 2a11 11 0 0 0 6 6l2-3 5 2v4a2 2 0 0 1-2 2A18 18 0 0 1 4 4a2 2 0 0 1 2-2z" fill="#ccc"/></svg>+1 (312) 555 0148</li>
        <li><svg width="12" height="14" viewBox="0 0 24 24"><rect x="2" y="5" width="20" height="14" fill="none" stroke="#ccc" stroke-width="2"/><path d="M2 6l10 7 10-7" stroke="#ccc" stroke-width="2" fill="none"/></svg>info@vitalquorra.com</li>
        <li><svg width="12" height="14" viewBox="0 0 24 24"><path d="M12 2a7 7 0 0 0-7 7c0 5 7 13 7 13s7-8 7-13a7 7 0 0 0-7-7z" fill="#ccc"/></svg>Vitalquorra<br>48 Larkmoor Avenue<br>Chicago, IL 60614</li>
      </ul>
    </div>
  </div>
</footer>
<div class="copyright">Copyright © 2014 Vitalquorra. All rights reserved.</div>

</body>
</html>
```